professional business card design for technology company

We are a small technology consulting firm, specialising in consulting based around Cloud and Managed services. Our colour scheme is yellow, blue and white, as you can see in the logos. Although we are based in melbourne australia, due to the nature of our work, our clients can be located anywhere. We are looking for a clean, professional, positive look - similar to our company logo

Target Market(s)

small business

Industry/Entity Type

Business

Contact Information for Business Card

eye catching, designed to incorporate some level of raised printing. Must contain website address, phone number, name and job title

Requirements
Must have
• Logo (attached) - use of the same colour scheme

```html
<!DOCTYPE html>
<html lang="en">
<head>
<meta charset="utf-8">
<title>Nuvara – Business Card</title>
<link rel="stylesheet" href="https://fonts.googleapis.com/css2?family=Montserrat:wght@400;600;700&family=Questrial&display=swap">
<style>
  :root {
    --backdrop: #1d1d1d;
    --card-white: #fbfbfb;
    --card-grey: #5c5c5c;
    --ink: #3a3a3a;
    --ink-soft: #555555;
    --brand-blue: #2f8fcf;
    --brand-yellow: #e3c01c;
    --brand-grey: #8a8a8a;
    --brand-light: #e6e6e6;
  }
  * { box-sizing: border-box; margin: 0; padding: 0; }
  html, body { width: 1200px; height: 873px; overflow: hidden; }
  body {
    background: var(--backdrop);
    position: relative;
    font-family: "Questrial", sans-serif;
  }
  .card {
    position: absolute;
    width: 520px;
    height: 297px;
    border-radius: 4px;
    box-shadow: 0 10px 30px rgba(0,0,0,.55);
  }
  .card--front { left: 60px; top: 150px; background: var(--card-white); }
  .card--back  { left: 620px; top: 426px; background: var(--card-grey); }

  .brand {
    position: absolute;
    display: flex;
    align-items: center;
    gap: 10px;
  }
  .brand__dot {
    border-radius: 50%;
    background: var(--brand-blue);
  }
  .brand__name {
    font-family: "Montserrat", sans-serif;
    font-weight: 700;
    letter-spacing: -0.5px;
  }
  .card--front .brand { right: 34px; top: 30px; }
  .card--front .brand__dot { width: 18px; height: 18px; }
  .card--front .brand__name { font-size: 30px; color: var(--brand-grey); }

  .divider {
    position: absolute;
    left: 200px; right: 34px; top: 84px;
    height: 2px;
    background: var(--brand-blue);
  }

  .person { position: absolute; left: 34px; top: 100px; }
  .person__name {
    font-family: "Montserrat", sans-serif;
    font-weight: 700;
    font-size: 17px;
    color: var(--ink);
  }
  .person__title { font-size: 15px; color: var(--ink-soft); margin-top: 2px; }

  .contacts {
    position: absolute;
    left: 34px; top: 160px; right: 24px;
    list-style: none;
    font-size: 13px;
    color: var(--ink-soft);
  }
  .contacts__row { display: flex; gap: 22px; margin-bottom: 12px; }
  .contact { display: flex; align-items: center; gap: 7px; white-space: nowrap; }
  .contact svg { width: 13px; height: 13px; fill: var(--brand-blue); flex: none; }

  .card--back .brand { right: 60px; top: 112px; }
  .card--back .brand__dot { width: 34px; height: 34px; }
  .card--back .brand__name { font-size: 52px; color: var(--brand-light); }
  .slogan {
    position: absolute;
    right: 60px; top: 190px;
    font-family: "Montserrat", sans-serif;
    font-weight: 600;
    font-size: 16px;
    letter-spacing: 3px;
    color: var(--brand-blue);
  }
</style>
</head>
<body>

<section class="card card--front" aria-label="Card front">
  <div class="brand"><span class="brand__dot"></span><span class="brand__name">Nuvara</span></div>
  <div class="divider"></div>

  <div class="person">
    <p class="person__name">Daniel K. Merrow</p>
    <p class="person__title">Broker/Owner</p>
  </div>

  <ul class="contacts">
    <li class="contacts__row">
      <span class="contact">
        <svg viewBox="0 0 16 16" aria-hidden="true"><path d="M3 1h3l1 4-2 1.5a9 9 0 0 0 4.5 4.5L11 9l4 1v3a2 2 0 0 1-2 2A12 12 0 0 1 1 3a2 2 0 0 1 2-2z"/></svg>
        555-201-4830
      </span>
      <span class="contact">
        <svg viewBox="0 0 16 16" aria-hidden="true"><path d="M4 0h8a1 1 0 0 1 1 1v14a1 1 0 0 1-1 1H4a1 1 0 0 1-1-1V1a1 1 0 0 1 1-1zm1 2v10h6V2z"/></svg>
        555-201-4831
      </span>
      <span class="contact">
        <svg viewBox="0 0 16 16" aria-hidden="true"><path d="M4 1h8v4h2a1 1 0 0 1 1 1v6h-3v3H4v-3H1V6a1 1 0 0 1 1-1h2zm1 1v3h6V2zm0 8v4h6v-4z"/></svg>
        555-201-4832
      </span>
    </li>
    <li class="contacts__row">
      <span class="contact">
        <svg viewBox="0 0 16 16" aria-hidden="true"><path d="M1 3h14v10H1zm1 1.2V12h12V4.2L8 9z"/></svg>
        dmerrow@mailbox.com
      </span>
      <span class="contact">
        <svg viewBox="0 0 16 16" aria-hidden="true"><path d="M6.5 9.5l3-3M5 8l-2 2a2.5 2.5 0 0 0 3.5 3.5l2-2M11 8l2-2A2.5 2.5 0 0 0 9.5 2.5l-2 2" stroke="#2f8fcf" stroke-width="1.8" fill="none"/></svg>
        www.nuvaracloud.com
      </span>
    </li>
    <li class="contacts__row">
      <span class="contact">
        <svg viewBox="0 0 16 16" aria-hidden="true"><path d="M8 1l7 6.5h-2V15H9.5v-4h-3v4H3V7.5H1z"/></svg>
        480 Harbor Lane #12, Bayview, Victoria 3000
      </span>
    </li>
  </ul>
</section>

<section class="card card--back" aria-label="Card back">
  <div class="brand"><span class="brand__dot"></span><span class="brand__name">Nuvara</span></div>
  <p class="slogan">YOUR SLOGAN / TAGLINE HERE</p>
</section>

</body>
</html>
```